Velmora Biz Card 2019

New business card for Velmora Property Inspections. We are a residential home inspection company in Arizona.

Target Market(s)

Real Estate

Font styles to use
Sans Serif

Requirements
Must have
• Glen Mirewick
• Home Inspector
• Velmora Property Inspections, LLC
• 480-555-0172
• glen@velmora-llc.example

```html
<!DOCTYPE html>
<html lang="en">
<head>
<meta charset="utf-8">
<title>Velmora Biz Card 2019</title>
<link rel="stylesheet" href="https://fonts.googleapis.com/css2?family=Oswald:wght@500&family=Open+Sans:wght@400&display=swap">
<style>
  :root {
    --backdrop: #5e5148;
    --card: #ffffff;
    --brand-green: #3fb24a;
    --brand-grey: #5f6062;
    --text-grey: #555658;
    --rule-grey: #c9c9c9;
    --photo-wall: #e4e6e2;
    --photo-shirt: #26324a;
    --skyline: #e6e6e6;
  }
  * { margin: 0; padding: 0; box-sizing: border-box; }
  html, body { width: 1200px; height: 960px; overflow: hidden; }
  body {
    position: relative;
    background: var(--backdrop);
    font-family: "Open Sans", Arial, sans-serif;
  }
  .card {
    position: absolute;
    left: 281px;
    width: 638px;
    height: 383px;
    background: var(--card);
    overflow: hidden;
  }
  .card--front { top: 73px; }
  .card--back { top: 495px; }

  .portrait {
    position: absolute;
    left: 0; top: 0;
    width: 317px; height: 100%;
    background: linear-gradient(180deg, var(--photo-wall) 0%, var(--photo-wall) 55%, var(--photo-shirt) 72%, var(--photo-shirt) 100%);
  }

  .wordmark {
    position: absolute;
    display: flex;
    flex-direction: column;
    align-items: center;
    font-family: "Oswald", Arial, sans-serif;
    font-weight: 500;
    color: var(--brand-grey);
    line-height: 1;
  }
  .wordmark__main {
    display: flex;
    align-items: center;
    gap: 10px;
    letter-spacing: 2px;
  }
  .wordmark__dot { background: var(--brand-green); }
  .wordmark__legal {
    letter-spacing: 2px;
    white-space: nowrap;
  }
  .card--front .wordmark { left: 317px; right: 0; top: 150px; }
  .card--front .wordmark__main { font-size: 38px; }
  .card--front .wordmark__dot { width: 20px; height: 20px; }
  .card--front .wordmark__legal { font-size: 12px; margin-top: 10px; }

  .card--back .wordmark { left: 52px; width: 260px; top: 150px; }
  .card--back .wordmark__main { font-size: 32px; }
  .card--back .wordmark__dot { width: 17px; height: 17px; }
  .card--back .wordmark__legal { font-size: 10.5px; margin-top: 9px; }

  .website {
    position: absolute;
    left: 317px; right: 0; top: 294px;
    text-align: center;
    font-family: "Oswald", Arial, sans-serif;
    font-weight: 500;
    font-size: 16px;
    letter-spacing: 1px;
    color: var(--text-grey);
  }

  .identity {
    position: absolute;
    left: 319px; top: 117px;
    padding-left: 25px;
    border-left: 2px solid var(--brand-green);
  }
  .identity__name {
    font-family: "Oswald", Arial, sans-serif;
    font-weight: 500;
    font-size: 22px;
    line-height: 1.1;
    letter-spacing: 0.5px;
    color: var(--text-grey);
    text-transform: uppercase;
  }
  .identity__role {
    font-size: 12.5px;
    color: var(--brand-green);
    line-height: 1.3;
  }

  .contact {
    position: absolute;
    left: 319px; top: 180px;
    padding-left: 25px;
    border-left: 2px solid var(--rule-grey);
    list-style: none;
  }
  .contact__item {
    display: flex;
    align-items: center;
    gap: 9px;
    height: 25.5px;
    font-size: 11.5px;
    color: var(--text-grey);
  }
  .contact__icon { width: 19px; height: 19px; flex: none; }

  .skyline {
    position: absolute;
    left: 0; right: 0; bottom: 0;
    height: 98px;
    background: linear-gradient(180deg, rgba(230,230,230,0) 0%, var(--skyline) 35%, var(--skyline) 100%);
  }
</style>
</head>
<body>

<section class="card card--front">
  <div class="portrait" role="img" aria-label="Portrait photo of Glen Mirewick in a navy company polo shirt"></div>
  <div class="wordmark">
    <span class="wordmark__main"><span class="wordmark__dot"></span><span>VELMORA</span></span>
    <span class="wordmark__legal">PROPERTY INSPECTIONS, LLC</span>
  </div>
  <p class="website">WWW.VELMORA-LLC.EXAMPLE</p>
</section>

<section class="card card--back">
  <div class="wordmark">
    <span class="wordmark__main"><span class="wordmark__dot"></span><span>VELMORA</span></span>
    <span class="wordmark__legal">PROPERTY INSPECTIONS, LLC</span>
  </div>

  <div class="identity">
    <h1 class="identity__name">Glen Mirewick</h1>
    <p class="identity__role">Home Inspector</p>
  </div>

  <ul class="contact">
    <li class="contact__item">
      <svg class="contact__icon" viewBox="0 0 20 20" aria-hidden="true">
        <circle cx="10" cy="10" r="10" fill="#3fb24a"/>
        <path d="M6.5 5.5l2 0 1 2.5-1.3 1c.6 1.2 1.6 2.2 2.8 2.8l1-1.3 2.5 1v2c0 .6-.5 1-1 1C9.5 14.5 5.5 10.5 5.5 6.5c0-.5.4-1 1-1z" fill="#fff"/>
      </svg>
      <span>480-555-0172</span>
    </li>
    <li class="contact__item">
      <svg class="contact__icon" viewBox="0 0 20 20" aria-hidden="true">
        <circle cx="10" cy="10" r="10" fill="#3fb24a"/>
        <rect x="5" y="6.5" width="10" height="7" fill="#fff"/>
        <path d="M5 6.5l5 4 5-4" fill="none" stroke="#3fb24a" stroke-width="1.2"/>
      </svg>
      <span>glen@velmora-llc.example</span>
    </li>
    <li class="contact__item">
      <svg class="contact__icon" viewBox="0 0 20 20" aria-hidden="true">
        <circle cx="10" cy="10" r="10" fill="#3fb24a"/>
        <path d="M10 4.5a3.6 3.6 0 0 0-3.6 3.6c0 2.7 3.6 7 3.6 7s3.6-4.3 3.6-7A3.6 3.6 0 0 0 10 4.5z" fill="#fff"/>
        <circle cx="10" cy="8.1" r="1.4" fill="#3fb24a"/>
      </svg>
      <span>4410 S. Juniper Ave. Tempe, AZ 85284</span>
    </li>
  </ul>

  <div class="skyline" role="img" aria-label="Faint grey city skyline illustration along the bottom edge"></div>
</section>

</body>
</html>
```